Upgrade 4 Images - Bid 1, then we can discuss the other 3

We have a four graphics that we use in various presentations and business proposals. We want to upgrade them to make them really pop and match the level of service we provide, without going overboard.

We're open to new ideas, but the general form and content should stay the same.

I'd like to have all four designed by the same person, but I'm assuming this bid will be for 1 of the four, and then the other three can be contracted as additions.

```html
<!DOCTYPE html>
<html lang="en">
<head>
<meta charset="utf-8">
<title>Service Maturity Model</title>
<link href="https://fonts.googleapis.com/css2?family=Barlow+Condensed:wght@700&family=Jost:wght@500&display=swap" rel="stylesheet">
<style>
  :root {
    --sky-top: #b9ecfd;
    --sky-bottom: #6ed5fb;
    --disc: #2ac7fa;
    --cap-navy: #0b1a7a;
    --cap-teal: #044a6d;
    --icon-faint: rgba(255,255,255,0.18);
    --white: #ffffff;
  }
  html, body {
    margin: 0;
    padding: 0;
    width: 1200px;
    height: 743px;
    overflow: hidden;
  }
  .canvas {
    width: 1200px;
    height: 743px;
    background: linear-gradient(180deg, var(--sky-top) 0%, var(--sky-bottom) 100%);
  }
  .diagram { display: block; }
  .stage-disc {
    fill: var(--disc);
    filter: drop-shadow(0 6px 10px rgba(0, 60, 110, 0.22));
  }
  .cap-navy { fill: var(--cap-navy); }
  .cap-teal { fill: var(--cap-teal); }
  .cap-icon { fill: var(--icon-faint); stroke: none; }
  .cap-icon-line { fill: none; stroke: var(--icon-faint); stroke-width: 6; }
  .stage-title {
    font-family: "Barlow Condensed", "Arial Narrow", sans-serif;
    font-weight: 700;
    font-size: 26px;
    letter-spacing: 0.3px;
    fill: var(--white);
    text-anchor: middle;
  }
  .stage-item {
    font-family: "Jost", "Futura", sans-serif;
    font-weight: 500;
    font-size: 16.5px;
    letter-spacing: 0.6px;
    fill: var(--white);
    text-anchor: middle;
  }
  .item-divider { stroke: rgba(255,255,255,0.45); stroke-width: 1; }
  .flow-mark {
    fill: none;
    stroke: var(--white);
    stroke-linecap: round;
    stroke-linejoin: round;
  }
  .plus-badge { fill: var(--white); }
  .plus-sign { stroke: var(--disc); stroke-width: 3.5; stroke-linecap: round; }
</style>
</head>
<body>
<div class="canvas">
  <svg class="diagram" width="1200" height="743" viewBox="0 0 1200 743" xmlns="http://www.w3.org/2000/svg">

    <!-- Ad hoc stage -->
    <g class="stage stage-adhoc">
      <circle class="stage-disc" cx="158" cy="373" r="121"/>
      <path class="cap-navy" d="M57 370 A101 101 0 0 1 259 370 Z"/>
      <circle class="cap-icon-line" cx="163" cy="322" r="35"/>
      <text class="stage-title" x="158" y="340">AD HOC</text>
      <text class="stage-item" x="155" y="396">Easy to Use</text>
      <text class="stage-item" x="157" y="420">Reduced errors</text>
      <text class="stage-item" x="155" y="445">24 Hour Window</text>
      <text class="stage-item" x="151" y="469">Job Queue</text>
    </g>

    <!-- Transition arrow -->
    <g class="flow-arrow">
      <line class="flow-mark" x1="338" y1="373" x2="455" y2="373" stroke-width="11"/>
      <polyline class="flow-mark" points="414,333 456,373 414,413" stroke-width="11"/>
    </g>

    <!-- Specialist stage -->
    <g class="stage stage-specialist">
      <circle class="stage-disc" cx="610" cy="191" r="121"/>
      <path class="cap-teal" d="M511 188 A99 99 0 0 1 709 188 Z"/>
      <text class="stage-title" x="611" y="157">SPECIALIST</text>
      <text class="stage-item" x="547" y="218">Workflow</text>
      <line class="item-divider" x1="600" y1="200" x2="600" y2="229"/>
      <text class="stage-item" x="662" y="218">Architecture</text>
      <text class="stage-item" x="608" y="249">Search Strategy</text>
      <text class="stage-item" x="608" y="280">Case Reporting</text>
    </g>

    <!-- Combine -->
    <g class="combine">
      <circle class="plus-badge" cx="605" cy="373" r="29"/>
      <line class="plus-sign" x1="590" y1="373" x2="620" y2="373"/>
      <line class="plus-sign" x1="605" y1="358" x2="605" y2="388"/>
    </g>

    <!-- Factory stage -->
    <g class="stage stage-factory">
      <circle class="stage-disc" cx="610" cy="553" r="121"/>
      <path class="cap-teal" d="M511 550 A99 99 0 0 1 709 550 Z"/>
      <g class="cap-icon">
        <rect x="586" y="468" width="9" height="28"/>
        <rect x="615" y="468" width="9" height="28"/>
        <path d="M573 545 V505 L597 493 V505 L621 493 V545 Z"/>
        <rect x="621" y="505" width="27" height="40"/>
      </g>
      <text class="stage-title" x="611" y="520">FACTORY</text>
      <text class="stage-item" x="608" y="582">Case Onboarding</text>
      <text class="stage-item" x="545" y="613">Roles</text>
      <line class="item-divider" x1="582" y1="593" x2="582" y2="622"/>
      <text class="stage-item" x="647" y="613">Data Re-use</text>
      <text class="stage-item" x="610" y="642">Resource Mgt</text>
    </g>

    <!-- Equals -->
    <g class="equals">
      <line class="flow-mark" x1="782" y1="350" x2="842" y2="350" stroke-width="10"/>
      <line class="flow-mark" x1="782" y1="379" x2="842" y2="379" stroke-width="10"/>
    </g>

    <!-- Enterprise stage -->
    <g class="stage stage-enterprise">
      <circle class="stage-disc" cx="1037" cy="373" r="121"/>
      <path class="cap-navy" d="M937 370 A101 101 0 0 1 1139 370 Z"/>
      <g class="cap-icon">
        <rect x="998" y="287" width="48" height="76"/>
        <rect x="1040" y="307" width="40" height="56"/>
        <rect x="994" y="360" width="88" height="5"/>
      </g>
      <text class="stage-title" x="1038" y="340">ENTERPRISE</text>
      <text class="stage-item" x="1038" y="395">Cross-case Analytics</text>
      <text class="stage-item" x="1034" y="419">Data Lakes</text>
      <text class="stage-item" x="1038" y="441">Matrixes Use</text>
      <text class="stage-item" x="1038" y="465">Recurring Jobs</text>
    </g>

  </svg>
</div>
</body>
</html>
```